Business card design, sleek & clean . For a notary loan signing business. I work with several lenders escrow officers etc . I am bilingual in Spanish , work 7 days a week to meet clients needs. Loan documents can be emailed for printing.

Not sure sleek clean logo

```html
<!DOCTYPE html>
<html lang="en">
<head>
<meta charset="utf-8">
<title>Marisol Quintero – Notary Public Business Card</title>
<link rel="stylesheet" href="https://fonts.googleapis.com/css2?family=Cormorant+Garamond:wght@500&family=Montserrat:wght@400;500&display=swap">
<style>
  :root {
    --stage: #828282;
    --navy: #000030;
    --ink: #0b0b3a;
    --gold: #c48f1a;
    --gold-dark: #8c6812;
    --gold-light: #e2ab22;
    --paper: #ffffff;
    --white: #ffffff;
  }
  * { margin: 0; padding: 0; box-sizing: border-box; }
  html, body {
    width: 1200px; height: 1200px; overflow: hidden;
    background: var(--stage);
  }
  .canvas { position: relative; width: 1200px; height: 1200px; }
  .card {
    position: absolute; left: 92px; width: 1016px; height: 580px;
  }
  .card-front { top: 10px; background: var(--navy); }
  .card-back { top: 610px; background: var(--paper); }

  .brand-name {
    font-family: "Cormorant Garamond", "Times New Roman", serif;
    font-weight: 500;
    color: var(--gold);
    text-transform: uppercase;
    white-space: nowrap;
    letter-spacing: 0.02em;
  }
  .front-brand {
    position: absolute; left: 0; right: 0; top: 262px;
    text-align: center; font-size: 50px; line-height: 1;
  }
  .front-title {
    position: absolute; right: 218px; top: 338px;
    font-family: "Montserrat", Arial, sans-serif;
    font-weight: 500; font-size: 17px; letter-spacing: 0.42em;
    color: var(--white);
  }

  .back-brand {
    position: absolute; left: 84px; top: 220px;
    font-size: 30px; line-height: 1;
  }
  .divider {
    position: absolute; left: 507px; top: 144px;
    width: 3px; height: 292px;
    background: linear-gradient(to bottom, var(--gold-light), var(--gold-dark));
  }
  .contact-list {
    position: absolute; left: 594px; top: 220px;
    list-style: none;
    font-family: "Montserrat", Arial, sans-serif;
    font-weight: 500; font-size: 20px;
  }
  .contact-item {
    display: flex; align-items: center; height: 31px;
    color: var(--gold);
  }
  .contact-item .icon {
    width: 20px; margin-right: 12px;
    display: inline-flex; justify-content: center; align-items: center;
  }
  .service-list {
    position: absolute; left: 594px; top: 295px;
    list-style: none;
    font-family: "Montserrat", Arial, sans-serif;
    font-weight: 500; font-size: 20px; color: var(--ink);
  }
  .service-item { display: flex; align-items: center; height: 30px; }
  .service-item .bar {
    width: 2px; height: 18px; background: var(--gold);
    margin: 0 20px 0 9px;
  }
  .tagline {
    position: absolute; left: 0; right: 0; top: 522px;
    text-align: center;
    font-family: "Montserrat", Arial, sans-serif;
    font-weight: 500; font-size: 20px; color: var(--ink);
  }
</style>
</head>
<body>
<main class="canvas">
  <section class="card card-front">
    <div class="brand-name front-brand">Marisol Quintero</div>
    <div class="front-title">NOTARY PUBLIC</div>
  </section>

  <section class="card card-back">
    <div class="brand-name back-brand">Marisol Quintero</div>
    <div class="divider"></div>

    <ul class="contact-list">
      <li class="contact-item">
        <span class="icon">
          <svg width="18" height="18" viewBox="0 0 24 24" aria-hidden="true">
            <path fill="#c48f1a" d="M6.6 10.8a15.1 15.1 0 0 0 6.6 6.6l2.2-2.2a1 1 0 0 1 1-.25 11.4 11.4 0 0 0 3.6.57 1 1 0 0 1 1 1V20a1 1 0 0 1-1 1A17 17 0 0 1 3 4a1 1 0 0 1 1-1h3.5a1 1 0 0 1 1 1c0 1.25.2 2.45.57 3.57a1 1 0 0 1-.25 1z"/>
          </svg>
        </span>
        <span class="value">mquintero_ca@mailpost.com</span>
      </li>
      <li class="contact-item">
        <span class="icon">@</span>
        <span class="value">(555) 014-2273</span>
      </li>
    </ul>

    <ul class="service-list">
      <li class="service-item"><span class="bar"></span>HABLO ESPANOL</li>
      <li class="service-item"><span class="bar"></span>NOTARY SIGNING AGENT</li>
    </ul>

    <p class="tagline">7 days a week to meet your clients needs</p>
  </section>
</main>
</body>
</html>
```